single page with calendar booking ability

a single web page that has the ability to book calendar times and dates, also needs to be able to link to my other business social media seamlessly. I don't want to get multiple developers and or agency's involved, I want you the web designer to design it and make sure it's up and works as described
. The boats we work on are between 20 feet to 40 feet, bow riders , cabin cruisers, and center consoles. The brands that we work on include but are not limited to Halvenk, Trindle, Pike dorrel, Oro vane, Quillard, Brevik, Talvo, and many more. Winterization and shrink wrapping is completely different than graphic wrapping, we do not do graphic's wrapping. Also, only 5% of our business will be auto detailing, the rest will be boats on trailers. Please ensure that the calendar booking system is intergraded and not a surprise to me later

Target Market(s)

Lakes region New Hampshire

Industry/Entity Type

marine

Coding

Coded - Design and coding required

Number of Pages Required

1 page

Colors
0054AA
0677BA
7BADD7
CADEEF
E8F1F8
00AB8E
00BBA5
67D7C9
C6EFE9
E9F9F6
EE7325
F08F49
F5BC92
FAE3D3
FDF4ED

Requirements
Must have
• calendar booking capability
Nice to have
• Pictures of boats being shrink wrapped for the winter season, Nice before and after pictures of boats detailed, only 5% of our business is auto detailing
Should not have
• Large yachts, lots of sail boats as we only do a few, graphics wrapping.. we don't graphic wrap

```html
<!DOCTYPE html>
<html lang="en">
<head>
<meta charset="UTF-8">
<title>Keelwood Marine And Auto</title>
<link href="https://fonts.googleapis.com/css2?family=Heebo:wght@400;500;700&display=swap" rel="stylesheet">
<style>
  :root {
    --sky-top: #a9d6f2;
    --sky-mid: #d5ebf8;
    --page-white: #ffffff;
    --ink: #3b3b3b;
    --ink-soft: #767676;
    --brand-red: #e8391d;
    --brand-blue: #0a98d8;
    --card-shadow: rgba(40, 70, 100, 0.14);
    --hull-grey: #c9d3dc;
    --hull-light: #eef2f5;
    --sea-blue: #6ea4cc;
    --icon-dark: #1e1e1e;
    --icon-grey: #8a8a8a;
  }
  * { margin: 0; padding: 0; box-sizing: border-box; }
  html, body { width: 1200px; height: 800px; overflow: hidden; }
  body {
    font-family: "Heebo", Arial, sans-serif;
    color: var(--ink);
    background: var(--page-white);
  }
  .page {
    position: relative;
    width: 1200px;
    height: 800px;
    overflow: hidden;
    background: linear-gradient(180deg, var(--sky-top) 0%, var(--sky-mid) 30%, #f2f8fc 55%, var(--page-white) 72%);
  }
  .brand {
    position: absolute;
    left: 89px;
    top: 40px;
    display: flex;
    align-items: center;
    gap: 8px;
    font-size: 22px;
    font-weight: 700;
    color: var(--brand-red);
  }
  .brand-dot {
    width: 14px; height: 14px; border-radius: 50%;
    background: var(--brand-red);
  }
  .top-nav {
    position: absolute;
    top: 29px;
    right: 111px;
    display: flex;
    align-items: center;
    font-size: 15px;
    font-weight: 500;
    color: var(--ink);
  }
  .nav-register { margin-right: 16px; }
  .nav-login {
    width: 97px; height: 30px;
    border: 1.6px solid var(--brand-blue);
    border-radius: 16px;
    display: flex; align-items: center; justify-content: center;
    margin-right: 13px;
  }
  .nav-lang { display: flex; align-items: center; gap: 3px; }
  .hero-photo {
    position: absolute;
    left: 485px;
    top: 182px;
    width: 715px;
    height: 392px;
    background:
      radial-gradient(ellipse 60% 30% at 55% 88%, var(--sea-blue) 0%, rgba(110,164,204,0) 70%),
      linear-gradient(180deg, rgba(255,255,255,0) 0%, var(--hull-light) 35%, var(--hull-grey) 70%, rgba(255,255,255,0) 100%);
    border-radius: 40% 0 0 30% / 50% 0 0 40%;
  }
  .hero-title {
    position: absolute;
    left: 87px;
    top: 291px;
    font-size: 64px;
    font-weight: 700;
    line-height: 62px;
    color: var(--ink);
  }
  .hero-title .accent { color: var(--brand-red); display: block; }
  .booking-card {
    position: absolute;
    left: 89px;
    top: 584px;
    width: 1022px;
    height: 132px;
    background: var(--page-white);
    border-radius: 14px;
    box-shadow: 0 14px 34px var(--card-shadow);
  }
  .booking-field { position: absolute; top: 40px; display: flex; align-items: flex-end; gap: 22px; }
  .field-label { font-size: 18px; color: var(--ink-soft); line-height: 22px; }
  .field-value { font-size: 24px; font-weight: 500; color: var(--ink); line-height: 30px; }
  .field-icon { width: 24px; height: 26px; margin-bottom: 3px; }
  .field-calendar { left: 44px; }
  .field-time { left: 291px; }
  .field-date { left: 499px; }
  .book-button {
    position: absolute;
    left: 766px;
    top: 44px;
    width: 215px;
    height: 46px;
    border-radius: 23px;
    background: var(--brand-blue);
    color: #fff;
    font-size: 19px;
    font-weight: 700;
    letter-spacing: 0.3px;
    display: flex; align-items: center; justify-content: center;
    border: none;
  }
  .copyright {
    position: absolute;
    left: 0; right: 0;
    top: 754px;
    text-align: center;
    font-size: 17px;
    font-weight: 500;
    color: var(--ink);
  }
</style>
</head>
<body>
<div class="page">
  <div class="brand"><span class="brand-dot"></span>Keelwood</div>

  <nav class="top-nav">
    <span class="nav-register">Register</span>
    <span class="nav-login">Login</span>
    <span class="nav-lang">En
      <svg width="10" height="7" viewBox="0 0 10 7"><path d="M1 1l4 4 4-4" fill="none" stroke="#3b3b3b" stroke-width="1.8"/></svg>
    </span>
  </nav>

  <div class="hero-photo" role="img" aria-label="Photo of two white work boats with grey and blue hulls cruising on the water"></div>

  <h1 class="hero-title"><span class="accent">Keelwood</span>Marine And<br>Auto</h1>

  <section class="booking-card">
    <div class="booking-field field-calendar">
      <div><div class="field-label">Calendar</div><div class="field-value">Fri, 22 Mar</div></div>
      <svg class="field-icon" viewBox="0 0 24 26"><rect x="0" y="3" width="24" height="23" rx="4" fill="var(--icon-dark)"/><rect x="5" y="0" width="3" height="6" rx="1" fill="var(--icon-dark)"/><rect x="16" y="0" width="3" height="6" rx="1" fill="var(--icon-dark)"/><g fill="#fff"><circle cx="7" cy="14" r="1.3"/><circle cx="12" cy="14" r="1.3"/><circle cx="17" cy="14" r="1.3"/><circle cx="7" cy="19" r="1.3"/><circle cx="12" cy="19" r="1.3"/><circle cx="17" cy="19" r="1.3"/></g></svg>
    </div>
    <div class="booking-field field-time">
      <div><div class="field-label">Times</div><div class="field-value">7, 00 Am</div></div>
      <svg class="field-icon" viewBox="0 0 26 26"><rect x="0" y="0" width="26" height="26" rx="5" fill="var(--icon-grey)"/><path d="M12 7v7l5 3" fill="none" stroke="var(--icon-dark)" stroke-width="2.4" stroke-linecap="round"/></svg>
    </div>
    <div class="booking-field field-date">
      <div><div class="field-label">Date</div><div class="field-value">July 3, Today</div></div>
      <svg class="field-icon" viewBox="0 0 24 26"><rect x="0" y="3" width="24" height="23" rx="4" fill="var(--icon-dark)"/><rect x="5" y="0" width="3" height="6" rx="1" fill="var(--icon-dark)"/><rect x="16" y="0" width="3" height="6" rx="1" fill="var(--icon-dark)"/><g fill="#fff"><circle cx="7" cy="14" r="1.3"/><circle cx="12" cy="14" r="1.3"/><circle cx="17" cy="14" r="1.3"/><circle cx="7" cy="19" r="1.3"/><circle cx="12" cy="19" r="1.3"/><circle cx="17" cy="19" r="1.3"/></g></svg>
    </div>
    <button class="book-button">BOOK NOW</button>
  </section>

  <footer class="copyright">©Copyright 2021 | All Rights Reseved</footer>
</div>
</body>
</html>
```